Business Card for Auto Dealership - Clean, sharp and professional

Please use the maroon logo with the grey background. Need a sharp, clean and professional business card for an Auto Dealer. In the files provides there is three different logos. I have not decided which one to go with yet. Right now I am favoring the grey/silver background. I would like my contact info on there and the website as well. I feel like less is more and want something simple, clean and sharp. Thank you in advance for your tie and effort! I also need email signature, letterhead, etc after this

Target Market(s)

Car buyers

Industry/Entity Type

Automotive

Contact Information for Business Card

Drew
555-214-7730
www.BriarvaleAutoLink.example
Drew@BriarvaleAutoLink.example

Font styles to use
Serif
Sans Serif

Requirements
Must have
• Please use the maroon logo with the grey background. Business Card Details and logo from files. Please stick to the logo colors

```html
<!DOCTYPE html>
<html lang="en">
<head>
<meta charset="utf-8">
<title>Briarvale Auto Link – Business Card</title>
<link href="https://fonts.googleapis.com/css2?family=Exo+2:wght@700&family=Ubuntu:wght@400&display=swap" rel="stylesheet">
<style>
  :root {
    --backdrop: #e9e6e2;
    --maroon: #4b1a20;
    --silver: #d9d7d5;
    --silver-edge: #efeeec;
    --ink-light: #ece6e4;
    --ink-soft: #d6c9c9;
  }
  * { margin: 0; padding: 0; box-sizing: border-box; }
  html, body {
    width: 1200px;
    height: 1047px;
    overflow: hidden;
    background: var(--backdrop);
  }
  .card {
    position: absolute;
    left: 100px;
    top: 223px;
    width: 1000px;
    height: 600px;
    background: var(--maroon);
    overflow: hidden;
    box-shadow: 0 18px 40px rgba(0,0,0,0.18);
  }
  .card__disc {
    position: absolute;
    left: 524px;
    top: 16px;
    width: 568px;
    height: 568px;
    border-radius: 50%;
    background: radial-gradient(circle at 40% 40%, var(--silver-edge), var(--silver) 70%);
  }
  .brand-name {
    position: absolute;
    left: 50px;
    top: 54px;
    font-family: "Exo 2", sans-serif;
    font-weight: 700;
    font-size: 46px;
    letter-spacing: 1px;
    color: var(--ink-light);
    text-transform: uppercase;
  }
  .person {
    position: absolute;
    left: 50px;
    top: 330px;
  }
  .person__name {
    font-family: "Exo 2", sans-serif;
    font-weight: 700;
    font-size: 38px;
    letter-spacing: 1px;
    color: var(--ink-light);
    text-transform: uppercase;
    line-height: 1.1;
  }
  .person__role {
    font-family: "Ubuntu", sans-serif;
    font-size: 21px;
    color: var(--ink-soft);
    margin-top: 6px;
  }
  .contact {
    position: absolute;
    left: 50px;
    top: 446px;
    list-style: none;
  }
  .contact__item {
    display: flex;
    align-items: center;
    height: 34px;
    font-family: "Ubuntu", sans-serif;
    font-size: 22px;
    color: var(--ink-soft);
  }
  .contact__icon {
    width: 20px;
    height: 20px;
    margin-right: 26px;
    fill: none;
    stroke: var(--ink-soft);
    stroke-width: 1.8;
  }
</style>
</head>
<body>
  <div class="card">
    <div class="card__disc"></div>

    <div class="brand-name">Briarvale Auto Link</div>

    <div class="person">
      <div class="person__name">Drew</div>
      <div class="person__role">Managing Director</div>
    </div>

    <ul class="contact">
      <li class="contact__item">
        <svg class="contact__icon" viewBox="0 0 20 20" aria-hidden="true">
          <path d="M2 8 Q10 2 18 8 L16 10 L13 8 L13 6 Q10 5 7 6 L7 8 L4 10 Z"/>
          <rect x="4" y="11" width="12" height="6" rx="1"/>
        </svg>
        555-214-7730
      </li>
      <li class="contact__item">
        <svg class="contact__icon" viewBox="0 0 20 20" aria-hidden="true">
          <circle cx="10" cy="10" r="8"/>
          <ellipse cx="10" cy="10" rx="3.5" ry="8"/>
          <line x1="2" y1="10" x2="18" y2="10"/>
        </svg>
        www.BriarvaleAutoLink.example
      </li>
      <li class="contact__item">
        <svg class="contact__icon" viewBox="0 0 20 20" aria-hidden="true">
          <rect x="2" y="4" width="16" height="12"/>
          <polyline points="2,4 10,11 18,4"/>
        </svg>
        Drew@BriarvaleAutoLink.example
      </li>
    </ul>
  </div>
</body>
</html>
```